Social Media Marketing website

Need website designed for social media marketing company PlumeVista.com
Do no currently have logo.
Pages:
Main
Services
Order
Contact
Please use dummy text for now. I will provide content to winner later to add.
Main page should clearly show the steps with some sort of graphic: Establish, Engage, Analyze.
Services provided (steps):
1) Establish social media presence
2) Social media management and advertising
3) Analyze and engage
Site should be simple, clean and attractive. Design examples:
http://brindlow.com/
http://www.quillmarkhub.com/
http://www.fenwaterlyx.com/
Be creative! It should not look like a template.
Updates
Updated examples.
Contact me for questions.
owen@plumevista.com
3) Analyze and engage
Advertising

```html
<!DOCTYPE html>
<html lang="en">
<head>
<meta charset="utf-8">
<title>PlumeVista.com – Social Media Marketing</title>
<link rel="stylesheet" href="https://fonts.googleapis.com/css2?family=Questrial&family=Didact+Gothic&display=swap">
<style>
  :root {
    --brand-blue: #1a8ad8;
    --gold: #c99a3a;
    --gold-light: #f7cf6e;
    --gold-mid: #f0bb48;
    --gold-deep: #e4a83a;
    --panel-yellow: #f2bd55;
    --grey-light: #ededeb;
    --grey-mid: #b9b6b1;
    --grey-dark: #8d8a86;
    --ink: #333333;
    --black: #000000;
    --white: #ffffff;
    --alert-red: #e0140e;
    --button-blue: #2a4f86;
  }
  * { box-sizing: border-box; margin: 0; padding: 0; }
  html, body { width: 1200px; height: 975px; overflow: hidden; background: var(--white); }
  body { position: relative; font-family: "Questrial", Arial, sans-serif; color: var(--ink); }
  .abs { position: absolute; }

  .site-name { left: 18px; top: 30px; font-size: 52px; color: var(--brand-blue); letter-spacing: 1px; white-space: nowrap; }
  .account-links { right: 12px; top: 76px; display: flex; gap: 30px; font-size: 26px; color: var(--gold); }

  .main-nav {
    left: 12px; top: 112px; width: 1176px; height: 80px;
    background: linear-gradient(to bottom, var(--gold-light), var(--gold-mid) 55%, var(--gold-deep));
    border-top: 2px solid #f9dc96;
  }
  .main-nav .item {
    position: absolute; top: 0; height: 80px; line-height: 78px; font-size: 27px;
    color: #b98c37; text-align: center; border-right: 2px solid #f8d993; white-space: nowrap;
  }
  .main-nav .item.active { color: var(--white); }
  .search-label { right: 320px; top: 24px; font-size: 27px; color: #b98c37; }
  .search-box {
    right: 36px; top: 22px; width: 270px; height: 38px; border-radius: 8px;
    background: linear-gradient(#d9d5c8, #f4f1e8); border: 2px solid #f8e3b0;
  }

  .sub-nav {
    left: 12px; top: 195px; width: 1176px; height: 128px;
    background: linear-gradient(to bottom, #fdfdfc, var(--grey-light) 25%, var(--grey-mid) 60%, var(--grey-light));
    border: 1px solid #c9c7c3;
  }
  .sub-nav .item { position: absolute; top: 40px; font-size: 25px; color: var(--ink); letter-spacing: -0.5px; white-space: nowrap; }
  .sub-nav svg { position: absolute; top: 14px; }

  .services { left: 12px; top: 330px; width: 573px; height: 608px; background: linear-gradient(135deg, #f4c766, var(--panel-yellow) 60%, #f7cf7a); }
  .services h2 { position: absolute; left: 24px; top: 44px; font-size: 34px; font-weight: 400; color: var(--white); white-space: nowrap; }
  .step { position: absolute; left: 93px; font-size: 24px; color: #9a7a3a; line-height: 34px; white-space: nowrap; }
  .step-icon { position: absolute; left: 24px; }

  .social-box {
    left: 12px; top: 708px; width: 485px; height: 128px; border-radius: 0 24px 24px 0;
    background: linear-gradient(#fafafa, #d3d1cd); box-shadow: 2px 4px 6px rgba(0,0,0,0.25);
  }
  .social-btn {
    position: absolute; left: 36px; width: 347px; height: 35px; border-radius: 4px;
    background: linear-gradient(#f6c968, #eeb445); font-size: 23px; line-height: 35px;
    text-align: center; color: var(--ink); font-family: "Didact Gothic", Arial, sans-serif;
  }
  .social-mark { position: absolute; left: 398px; width: 44px; height: 38px; border-radius: 5px; }
  .free-note { left: 33px; top: 865px; font-size: 21px; color: #a87f32; white-space: nowrap; }

  .join-panel { left: 585px; top: 330px; width: 603px; height: 608px; background: linear-gradient(to bottom, var(--black) 75%, #3a3a3a); }
  .photo-slot { left: 600px; top: 360px; width: 267px; height: 219px; border: 4px solid #c79a4a; background: radial-gradient(circle at 50% 55%, #b9703e, #8c5530 55%, #d8cdbf); }
  .join-title { left: 585px; top: 594px; width: 312px; text-align: center; font-size: 32px; line-height: 42px; color: var(--white); font-weight: 400; }
  .tip { position: absolute; left: 636px; font-family: "Didact Gothic", Arial, sans-serif; }
  .tip .label { font-size: 18px; color: #f2b845; line-height: 20px; }
  .tip .more { font-size: 13px; color: var(--white); margin-top: 3px; }
  .tip-icon { position: absolute; left: 596px; }

  .login-heading { left: 926px; top: 362px; font-size: 19px; color: var(--alert-red); letter-spacing: 1px; }
  .login-box {
    left: 915px; top: 394px; width: 273px; height: 139px; border-radius: 24px 0 0 24px;
    background: linear-gradient(#f2f1ef, #bdbab5);
  }
  .login-box .field-label { position: absolute; left: 48px; font-size: 21px; color: var(--ink); font-family: "Didact Gothic", Arial, sans-serif; }
  .login-box .field { position: absolute; left: 47px; width: 191px; height: 24px; border-radius: 5px; background: var(--white); border: 1px solid #9c9994; }
  .forgot { left: 921px; top: 540px; font-size: 19px; color: var(--alert-red); letter-spacing: 1px; white-space: nowrap; }
  .signup-btn {
    left: 1005px; top: 580px; width: 90px; height: 38px; border-radius: 6px;
    background: linear-gradient(#6b8ec4, var(--button-blue)); border: 2px solid #c9d3e4;
    color: var(--white); font-size: 20px; font-weight: 700; text-align: center; line-height: 33px;
  }

  .copyright { left: 0; top: 950px; width: 1200px; text-align: center; font-size: 12px; color: #a87f32; }
</style>
</head>
<body>

<header>
  <div class="abs site-name">PlumeVista.com</div>
  <nav class="abs account-links"><span>Login</span><span>Sign up</span></nav>
</header>

<nav class="abs main-nav">
  <div class="item active" style="left:0;width:158px;">MAIN</div>
  <div class="item" style="left:158px;width:153px;">SERVICE</div>
  <div class="item" style="left:311px;width:152px;">ORDER</div>
  <div class="item" style="left:463px;width:152px;">CONTACT</div>
  <div class="abs search-label">Search</div>
  <div class="abs search-box">
    <svg class="abs" style="right:4px;top:3px" width="30" height="28" viewBox="0 0 30 28"><circle cx="12" cy="12" r="8" fill="none" stroke="#777" stroke-width="2.5"/><line x1="18" y1="18" x2="27" y2="26" stroke="#777" stroke-width="3"/></svg>
  </div>
</nav>

<nav class="abs sub-nav">
  <svg style="left:48px" width="50" height="60" viewBox="0 0 50 60"><path d="M4 34 L16 54 L46 4 L16 40 Z" fill="#777"/></svg>
  <div class="item" style="left:82px">HOW IT WORKS ?</div>
  <svg style="left:348px" width="50" height="60" viewBox="0 0 50 60"><path d="M4 34 L16 54 L46 4 L16 40 Z" fill="#777"/></svg>
  <div class="item" style="left:390px">MEMBERS</div>
  <svg style="left:602px" width="50" height="60" viewBox="0 0 50 60"><path d="M4 34 L16 54 L46 4 L16 40 Z" fill="#777"/></svg>
  <div class="item" style="left:644px">PRODUCT</div>
  <svg style="left:860px" width="50" height="60" viewBox="0 0 50 60"><path d="M4 34 L16 54 L46 4 L16 40 Z" fill="#777"/></svg>
  <div class="item" style="left:903px">GET CONTENT</div>
</nav>

<main>
  <section class="abs services">
    <h2>SERVICE PROVIDED (STEPS)</h2>
    <svg class="step-icon" style="top:108px" width="48" height="52" viewBox="0 0 48 52"><rect x="10" y="2" width="34" height="30" fill="#8d8a86"/><rect x="3" y="8" width="34" height="30" fill="#6b6966"/><path d="M14 38 L20 48 L24 38 Z" fill="#6b6966"/></svg>
    <div class="step" style="top:116px">Establish social media presence</div>
    <svg class="step-icon" style="top:186px" width="46" height="50" viewBox="0 0 46 50"><ellipse cx="22" cy="28" rx="20" ry="18" fill="#6b6966"/><ellipse cx="22" cy="22" rx="20" ry="18" fill="#9a9792"/><text x="22" y="31" font-size="24" text-anchor="middle" fill="#fff" font-family="Arial, sans-serif">$</text></svg>
    <div class="step" style="top:186px">Social media management and<br>advertising</div>
    <svg class="step-icon" style="top:278px" width="46" height="50" viewBox="0 0 46 50"><rect x="2" y="2" width="42" height="46" rx="6" fill="#7a7874"/><rect x="5" y="5" width="36" height="40" rx="4" fill="#a9a6a1"/><path d="M14 36 L16 28 L30 12 L34 16 L20 32 Z" fill="none" stroke="#fff" stroke-width="2.5"/></svg>
    <div class="step" style="top:282px">Analyze and engage</div>
  </section>

  <div class="abs social-box">
    <div class="social-btn" style="top:21px">Sign in with Friendlio</div>
    <div class="social-mark" style="top:19px;background:#3c5a9a"></div>
    <div class="social-btn" style="top:69px">Sign in with Chirpnet</div>
    <div class="social-mark" style="top:67px;background:#5bbfe8"></div>
  </div>
  <p class="abs free-note">Its totally free to be registered with us and easy to use</p>

  <section class="abs join-panel"></section>
  <div class="abs photo-slot" role="img" aria-label="Photo of clay figures standing in a circle with arms linked"></div>
  <h2 class="abs join-title">JOIN WITH US AND BUILD YOUR NETWORK</h2>

  <svg class="tip-icon" style="top:720px" width="28" height="26" viewBox="0 0 28 26"><path d="M3 22 L5 15 L19 2 L25 8 L11 21 Z" fill="#f2b845" stroke="#a87a22" stroke-width="1.5"/></svg>
  <div class="tip" style="top:732px"><div class="label">Business success tips</div><div class="more">Learn more....</div></div>
  <svg class="tip-icon" style="top:770px" width="28" height="26" viewBox="0 0 28 26"><path d="M3 22 L5 15 L19 2 L25 8 L11 21 Z" fill="#f2b845" stroke="#a87a22" stroke-width="1.5"/></svg>
  <div class="tip" style="top:784px"><div class="label">social network for<br>business</div><div class="more">Learn more....</div></div>
  <svg class="tip-icon" style="top:838px" width="28" height="26" viewBox="0 0 28 26"><path d="M3 22 L5 15 L19 2 L25 8 L11 21 Z" fill="#f2b845" stroke="#a87a22" stroke-width="1.5"/></svg>
  <div class="tip" style="top:852px"><div class="label">how to build network</div><div class="more">Learn more....</div></div>

  <div class="abs login-heading">Log in</div>
  <form class="abs login-box">
    <div class="field-label" style="top:5px">User</div>
    <div class="field" style="top:33px"></div>
    <div class="field-label" style="top:62px">Password</div>
    <div class="field" style="top:91px"></div>
  </form>
  <div class="abs forgot">Forgot your password?</div>
  <div class="abs signup-btn">Sign Up</div>
</main>

<footer class="abs copyright">Copyright 2011 - PlumeVista.com- All Right Reserved</footer>

</body>
</html>
```